Wade Merriton business card design front/back

Need a professional and eye catch design capable of making a lasting impression on clients I meet for the first time
Very bold and awesome look. Nothing childish or playful. I want the professionals working on this to make it as strong and professional look
I would like my name to say Wade Merriton
Job title is a NDT Inspector/ Consultant
My cell is 555.207.3914
Office is 555.318.4720
Fax is 555.318.4721
4817 Larkspur Valley Rd Midland Tx 79705
Wade_Merriton42@mailvesta.com

Target Market(s)

Clients in a higher up position of an oil & gas company.

Industry/Entity Type

Oil And Gas

Contact Information for Business Card

On the back of my business card I would like The word "Southern" in the company name to be bigger & bolder than the other 2 words "Weldcheck Services" underneath it

Colors
ffffff
ec1f27
f04a50
3176b5
0655a3
000000
0792cd
33a6d7
81c8e6

Requirements
Must have
• On the business card I need information such as
• Southern Weldcheck Services
• Wade Merriton
• NDT Inspector/ Consultant
• Mobile: 555-207-3915
• Fax:555-318-4721
• Office:555-318-4720
• 4817 Larkspur Valley Rd Harlow Springs, Wx 79705
• Wade_Merriton42@mailvesta.com
Nice to have
• I only want the back of my card to say Southern Weldcheck Services with a logo
Should not have
• On the front of my card. I don't want my company name fully typed out. Instead I would like it abbreviated and just put S.W.S
• Feel free to use whatever colors. It really doesn't mater but I would like to see the name on the back to be red and blue with a white background

```html
<!DOCTYPE html>
<html lang="en">
<head>
<meta charset="utf-8">
<title>Southern Weldcheck Services – Business Card</title>
<link rel="stylesheet" href="https://fonts.googleapis.com/css2?family=Source+Sans+3:wght@400;600;700&display=swap">
<style>
  :root {
    --navy: #2b3a66;
    --red: #c8323a;
    --ink: #2a2f3a;
    --paper: #ffffff;
    --backdrop: #e9e7e3;
    --rule: #3a4a78;
  }
  * { box-sizing: border-box; margin: 0; padding: 0; }
  html, body { width: 1200px; height: 800px; overflow: hidden; }
  body {
    background: var(--backdrop);
    font-family: "Source Sans 3", sans-serif;
    display: flex;
    align-items: center;
    justify-content: center;
    gap: 48px;
  }
  .card {
    width: 520px;
    height: 300px;
    background: var(--paper);
    border-radius: 18px;
    box-shadow: 0 6px 18px rgba(0,0,0,0.12);
    position: relative;
    overflow: hidden;
  }

  /* Back side: company name with mark */
  .card-back { display: flex; align-items: center; justify-content: center; }
  .brand { display: flex; align-items: center; gap: 18px; }
  .brand-mark {
    width: 92px; height: 92px; border-radius: 50%;
    background: var(--navy); flex: none;
  }
  .brand-name { color: var(--navy); font-weight: 600; line-height: 1; }
  .brand-name .primary { display: block; font-size: 64px; letter-spacing: -0.5px; }
  .brand-name .secondary { display: block; font-size: 19px; letter-spacing: 5px; margin-top: 8px; }

  /* Front side: contact details */
  .card-front { padding: 26px 34px; }
  .front-brand {
    position: absolute; top: 26px; right: 34px;
    display: flex; align-items: center; gap: 12px;
  }
  .front-brand .brand-mark { width: 58px; height: 58px; }
  .front-brand .initials { color: var(--red); font-size: 46px; font-weight: 600; line-height: 1; }

  .identity {
    margin-top: 84px;
    border-left: 6px solid var(--rule);
    padding-left: 10px;
  }
  .identity .name { color: var(--navy); font-size: 22px; font-weight: 600; line-height: 1.05; }
  .identity .title { color: var(--red); font-size: 15px; font-weight: 600; }

  .contact { list-style: none; margin-top: 14px; }
  .contact li {
    display: flex; align-items: center; gap: 9px;
    color: var(--ink); font-size: 14.5px; font-weight: 600; line-height: 1.38;
  }
  .contact svg { width: 13px; height: 13px; fill: var(--red); flex: none; }
</style>
</head>
<body>

  <section class="card card-back" aria-label="Card back">
    <div class="brand">
      <span class="brand-mark" aria-hidden="true"></span>
      <div class="brand-name">
        <span class="primary">Southern</span>
        <span class="secondary">Weldcheck Services</span>
      </div>
    </div>
  </section>

  <section class="card card-front" aria-label="Card front">
    <div class="front-brand">
      <span class="brand-mark" aria-hidden="true"></span>
      <span class="initials">S.W.S</span>
    </div>

    <div class="identity">
      <p class="name">Wade Merriton</p>
      <p class="title">NDT Inspector/ Consultant</p>
    </div>

    <ul class="contact">
      <li>
        <svg viewBox="0 0 16 16" aria-hidden="true"><path d="M4 0h8a1 1 0 0 1 1 1v14a1 1 0 0 1-1 1H4a1 1 0 0 1-1-1V1a1 1 0 0 1 1-1zm1 2v10h6V2z"/></svg>
        555-207-3915
      </li>
      <li>
        <svg viewBox="0 0 16 16" aria-hidden="true"><path d="M4 0h8v4H4zM1 5h14a1 1 0 0 1 1 1v6h-3v4H3v-4H0V6a1 1 0 0 1 1-1zm4 6v3h6v-3z"/></svg>
        555-318-4721
      </li>
      <li>
        <svg viewBox="0 0 16 16" aria-hidden="true"><path d="M3 1l3 3-2 2c1 2 4 5 6 6l2-2 3 3-2 3C7 16 0 9 0 3z"/></svg>
        555-318-4720
      </li>
      <li>
        <svg viewBox="0 0 16 16" aria-hidden="true"><path d="M0 3h16v1L8 9 0 4zm0 3l8 5 8-5v7H0z"/></svg>
        Wade_Merriton42@mailvesta.com
      </li>
      <li>
        <svg viewBox="0 0 16 16" aria-hidden="true"><path d="M8 0a5.5 5.5 0 0 1 5.5 5.5C13.5 10 8 16 8 16S2.5 10 2.5 5.5A5.5 5.5 0 0 1 8 0zm0 3.5a2 2 0 1 0 0 4 2 2 0 0 0 0-4z"/></svg>
        4817 Larkspur Valley Rd Harlow Springs, Wx 79705
      </li>
    </ul>
  </section>

</body>
</html>
```